Escape Room Flyer Design - Start up. A5

Flyer is for letterbox drops to get interest and let people know that our business exists and to a lesser extent what an escape room is. We have 1 room (the miller's shadows) and a second room coming soon (Varuna's Vault). I have attached our logo and 2 flyers that I have seen in the past that I really like the design of.
Whether you are having a night out with friends or family, celebrating a special event, planning a team-building activity, or simply wanting a diversion from the doldrums of your workweek, The Lock Box will provide you an unforgettable live-action gaming experience.

Target Market(s)

18-25

Industry/Entity Type

Entertainment

Requirements
Must have
• Logo. Phone number 0417 265 839. Website. www.thelockboxhartwell.com
Bookings essential.
Nice to have
• Mystery, a little bit on the darker side than bright colourful and blocky.
"Many Will Enter…Few Will Escape" tag line
60 minute game. Team work. 2-6 players. All ages.
Should not have
• Cartoons, characters, people

```html
<!DOCTYPE html>
<html lang="en">
<head>
<meta charset="utf-8">
<title>The Lock Box — Escape Room Flyer</title>
<link rel="stylesheet" href="https://fonts.googleapis.com/css2?family=Bungee&family=Montserrat:wght@500&display=swap">
<style>
  :root {
    --frame: #f8e3a6;
    --cream: #fdebc0;
    --gold: #f6d27a;
    --gold-soft: #f4c96e;
    --night: #1c2a33;
    --teal: #3b5a57;
    --amber: #b7742a;
    --rust: #c98a34;
  }
  * { box-sizing: border-box; margin: 0; padding: 0; }
  html, body { width: 857px; height: 1200px; overflow: hidden; background: var(--frame); }
  .flyer {
    position: relative;
    width: 857px;
    height: 1200px;
    background: var(--frame);
    padding: 10px;
    font-family: "Bungee", sans-serif;
  }
  .scene {
    position: absolute;
    inset: 10px;
    background:
      radial-gradient(ellipse 60% 30% at 60% 28%, rgba(170, 200, 190, 0.35), transparent 70%),
      linear-gradient(180deg, var(--night) 0%, var(--teal) 28%, #5b5a43 48%, var(--amber) 75%, var(--rust) 100%);
  }
  .brand-mark {
    position: absolute;
    left: 628px;
    top: 120px;
    width: 200px;
    display: flex;
    align-items: center;
    gap: 8px;
    color: var(--gold);
    font-size: 21px;
    line-height: 1;
  }
  .brand-mark .dot {
    width: 18px; height: 18px; border-radius: 50%;
    background: var(--gold); flex: none;
  }
  .brand-faint {
    position: absolute;
    left: 0; right: 0;
    top: 560px;
    text-align: center;
    font-size: 64px;
    color: rgba(200, 120, 40, 0.22);
  }
  .tagline span {
    position: absolute;
    color: var(--cream);
    line-height: 1;
    white-space: nowrap;
  }
  .t-many   { left: 70px;  top: 128px; font-size: 74px; }
  .t-will-1 { left: 100px; top: 276px; font-size: 26px; }
  .t-enter  { left: 210px; top: 214px; font-size: 92px; }
  .t-few    { left: 96px;  top: 328px; font-size: 70px; }
  .t-will-2 { left: 316px; top: 348px; font-size: 27px; }
  .t-escape { left: 322px; top: 392px; font-size: 92px; letter-spacing: -2px; }
  .features {
    position: absolute;
    left: 103px;
    top: 612px;
    list-style: none;
    color: var(--gold);
    font-size: 28px;
    line-height: 1;
  }
  .features li { height: 68.5px; }
  .features li::before { content: "."; }
  .booking {
    position: absolute;
    left: 160px;
    top: 940px;
    width: 540px;
  }
  .booking .phone-icon {
    position: absolute; left: 0; top: 12px; width: 54px; height: 84px;
  }
  .booking .cta {
    position: absolute; left: 80px; top: 0;
    font-size: 70px; line-height: 1; color: var(--gold); white-space: nowrap;
  }
  .booking .number {
    position: absolute; left: 146px; top: 84px;
    font-size: 33px; line-height: 1; color: var(--gold); white-space: nowrap;
  }
  .website {
    position: absolute;
    left: 246px;
    top: 1131px;
    display: flex;
    align-items: center;
    gap: 14px;
    font-family: "Montserrat", sans-serif;
    font-weight: 500;
    font-size: 18.5px;
    color: var(--gold-soft);
    letter-spacing: 0.3px;
  }
  .website svg { width: 26px; height: 26px; }
</style>
</head>
<body>
<main class="flyer">
  <div class="scene" role="img" aria-label="Dim underground corridor with corrugated walls and ceiling lights fading from dark teal into amber"></div>

  <div class="brand-faint" aria-hidden="true">The Lock Box</div>

  <div class="brand-mark"><span class="dot"></span><span>The Lock Box</span></div>

  <h1 class="tagline">
    <span class="t-many">many</span>
    <span class="t-will-1">will</span>
    <span class="t-enter">enter</span>
    <span class="t-few">few</span>
    <span class="t-will-2">will</span>
    <span class="t-escape">escape</span>
  </h1>

  <ul class="features">
    <li>60 minute game</li>
    <li>team work</li>
    <li>2-6 players</li>
    <li>all ages</li>
  </ul>

  <section class="booking">
    <svg class="phone-icon" viewBox="0 0 54 84" fill="none" stroke="var(--gold)" stroke-width="4" stroke-linecap="round">
      <rect x="4" y="20" width="32" height="58" rx="5" transform="rotate(-14 20 49)"/>
      <circle cx="27" cy="70" r="2.5" fill="var(--gold)" stroke="none"/>
      <path d="M38 14 a10 10 0 0 1 8 10"/>
      <path d="M40 4 a20 20 0 0 1 12 18"/>
    </svg>
    <div class="cta">Book now!</div>
    <div class="number">0417 265 839</div>
  </section>

  <footer class="website">
    <svg viewBox="0 0 26 26" fill="none" stroke="var(--gold-soft)" stroke-width="1.6">
      <circle cx="13" cy="13" r="11.5"/>
      <ellipse cx="13" cy="13" rx="5" ry="11.5"/>
      <path d="M1.5 13h23M3.5 7h19M3.5 19h19M13 1.5v23"/>
    </svg>
    <span>WWW.THELOCKBOXHARTWELL.COM</span>
  </footer>
</main>
</body>
</html>
```